RPN FORMED

building services
decks
pergola
renovation
extensions
general building

Target Market(s)

middle to upper class

Industry/Entity Type

building

Contact Information for Business Card

my details 0438917264 tkbarrow47@mailvora.com BLD581047

Font styles to use
Serif

Colors
00AB8E
00BBA5
67D7C9
C6EFE9
E9F9F6

Requirements
Must have
• logo on the front and details on the back
Nice to have
• sharp and clean lines

```html
<!DOCTYPE html>
<html lang="en">
<head>
<meta charset="utf-8">
<title>RPN FORMED – Business Card</title>
<link rel="stylesheet" href="https://fonts.googleapis.com/css2?family=Lora:wght@400;500;600;700&display=swap">
<style>
  :root {
    --teal-deep: #00AB8E;
    --teal: #00BBA5;
    --teal-mid: #67D7C9;
    --teal-pale: #C6EFE9;
    --teal-mist: #E9F9F6;
    --card-white: #ffffff;
    --ink: #0e4a42;
  }
  html, body {
    margin: 0;
    padding: 0;
    width: 1200px;
    height: 897px;
    overflow: hidden;
    background: var(--teal-pale);
    font-family: "Lora", serif;
  }
  .canvas {
    position: relative;
    width: 1200px;
    height: 897px;
  }
  .card {
    position: absolute;
    left: 329px;
    width: 543px;
    height: 310px;
    overflow: hidden;
  }
  .card--front { top: 108px; background: var(--card-white); color: var(--ink); }
  .card--back  { top: 479px; background: var(--teal-deep); }

  .brand-name {
    position: absolute;
    right: 34px;
    top: 30px;
    margin: 0;
    font-size: 34px;
    font-weight: 700;
    letter-spacing: 1px;
    line-height: 1;
    color: var(--teal-deep);
  }
  .name-marker {
    position: absolute;
    left: 0;
    top: 134px;
    width: 9px;
    height: 31px;
    background: var(--teal-deep);
  }
  .person {
    position: absolute;
    left: 33px;
    top: 130px;
  }
  .person__name {
    margin: 0;
    font-size: 19px;
    font-weight: 600;
    letter-spacing: 0.5px;
    line-height: 1.1;
    color: var(--ink);
  }
  .person__role {
    margin: 2px 0 0;
    font-size: 13px;
    font-weight: 400;
    letter-spacing: 0.6px;
    color: var(--teal-deep);
  }
  .divider {
    position: absolute;
    left: 33px;
    top: 179px;
    width: 286px;
    height: 1px;
    background: var(--teal-mid);
  }
  .services {
    position: absolute;
    right: 34px;
    top: 170px;
    text-align: right;
  }
  .services__title {
    margin: 0 0 4px;
    font-size: 14px;
    font-weight: 600;
    line-height: 18px;
    color: var(--teal-deep);
  }
  .services__list {
    list-style: none;
    margin: 0;
    padding: 0;
  }
  .services__item {
    font-size: 13.5px;
    line-height: 17.8px;
    display: flex;
    justify-content: flex-end;
    align-items: center;
    gap: 7px;
  }
  .services__item::after {
    content: "";
    width: 9px;
    height: 9px;
    border-radius: 50%;
    background: var(--teal);
  }
  .contact {
    position: absolute;
    left: 33px;
    top: 211px;
    font-size: 13.5px;
    line-height: 18px;
  }
  .contact__row {
    display: flex;
    align-items: center;
    gap: 6px;
  }
  .contact__icon { width: 9px; height: 9px; }
  .footer-bands {
    position: absolute;
    left: 0;
    bottom: 0;
    width: 543px;
    height: 33px;
  }
  .licence {
    position: absolute;
    left: 33px;
    bottom: 8px;
    margin: 0;
    font-size: 13px;
    letter-spacing: 1.8px;
    color: var(--card-white);
  }
  .back-brand {
    position: absolute;
    left: 0;
    right: 0;
    top: 50%;
    transform: translateY(-50%);
    margin: 0;
    text-align: center;
    font-size: 54px;
    font-weight: 700;
    letter-spacing: 2px;
    color: var(--teal-mist);
  }
</style>
</head>
<body>
<main class="canvas">
  <section class="card card--front" aria-label="Business card front">
    <h1 class="brand-name">RPN FORMED</h1>

    <span class="name-marker"></span>
    <div class="person">
      <p class="person__name">DANIEL HARPER</p>
      <p class="person__role">DIRECTOR</p>
    </div>

    <span class="divider"></span>

    <div class="services">
      <p class="services__title">BUILDING SERVICES</p>
      <ul class="services__list">
        <li class="services__item">Decks</li>
        <li class="services__item">Pergola</li>
        <li class="services__item">Renovation</li>
        <li class="services__item">Extensions</li>
        <li class="services__item">General building</li>
      </ul>
    </div>

    <div class="contact">
      <div class="contact__row">
        <svg class="contact__icon" viewBox="0 0 10 10" aria-hidden="true">
          <path d="M2.2 0.8 L3.6 2.6 L2.8 3.6 Q3.8 5.8 6.2 7.2 L7.2 6.4 L9.2 7.8 L8.2 9.4 Q4.4 9 1.8 5.6 Q0.6 3.6 0.8 1.8 Z" fill="none" stroke="#00AB8E" stroke-width="1"/>
        </svg>
        <span>0438917264</span>
      </div>
      <div class="contact__row">
        <svg class="contact__icon" viewBox="0 0 10 10" aria-hidden="true">
          <rect x="0.6" y="2" width="8.8" height="6.2" fill="none" stroke="#00AB8E" stroke-width="1"/>
          <path d="M0.6 2 L5 5.6 L9.4 2" fill="none" stroke="#00AB8E" stroke-width="1"/>
        </svg>
        <span>tkbarrow47@mailvora.com</span>
      </div>
    </div>

    <svg class="footer-bands" viewBox="0 0 543 33" aria-hidden="true">
      <polygon points="0,0 221,0 254,33 0,33" fill="#00AB8E"/>
      <polygon points="248,23 543,23 543,33 258,33" fill="#67D7C9"/>
    </svg>
    <p class="licence">BLD581047</p>
  </section>

  <section class="card card--back" aria-label="Business card back">
    <h2 class="back-brand">RPN FORMED</h2>
  </section>
</main>
</body>
</html>
```